Local Horticulturalist needs Business card design

Meridale Gardening would like to update our existing business card and utilize our new logo (design attached)....we specialize in getting the best out of our customers yard with professional maintenance programs, expert pruning and hedging and garden restorations.
Utilizing colors from attached logo I would like a design that implies professionalism and if possible our businesses love of restoration through plants.
I also sometimes write down for my customers a start date and price on the back of my current card
Target Market(s)
Home owners
Contractors
Industry/Entity Type
Gardener
Contact Information for Business Card
Trevor Kalbrook | Horticulturalist
ph: 0452739186
meridalegard@fernpost.com
www.meridalegardening.com.au
Requirements
Must have
- crucial information easy to read
- incorporate current logo
- Horticulturalist listed preferably near name
Nice to have
- currently I write a job start date and price on the back of my current card so something that integrates this would be beneficial
Should not have
- be pretty or flowerey
- be too white or basic

```html
<!DOCTYPE html>
<html lang="en">
<head>
<meta charset="utf-8">
<title>Meridale Gardening – Business Card</title>
<link href="https://fonts.googleapis.com/css2?family=Arimo:wght@400;700&family=PT+Sans:wght@400;700&display=swap" rel="stylesheet">
<style>
  :root{
    --olive:#86993a;
    --olive-light:#a9c34f;
    --olive-dark:#738629;
    --leaf:#7cbb2a;
    --bark:#7b6a55;
    --paper-a:#eefac6;
    --paper-b:#fbfff0;
    --canvas:#f2f2f2;
    --white:#ffffff;
  }
  *{margin:0;padding:0;box-sizing:border-box}
  html,body{width:1200px;height:1000px;overflow:hidden;background:var(--canvas)}
  body{position:relative;font-family:"Arimo",Arial,sans-serif}

  .card{position:absolute;width:684px;height:367px;overflow:hidden;
    background:linear-gradient(110deg,var(--paper-a) 0%,var(--paper-b) 55%,var(--paper-a) 100%)}
  .card--front{left:107px;top:108px}
  .card--back{left:433px;top:540px;height:367px}

  .band{position:absolute;left:0;width:100%;
    background:linear-gradient(100deg,var(--olive) 0%,var(--olive-light) 35%,var(--olive) 60%,var(--olive-light) 85%,var(--olive) 100%)}
  .band--top{top:0;height:37px}
  .band--bottom{bottom:0;height:40px}

  .watermark-circle{position:absolute;border-radius:50%;background:var(--leaf);opacity:.14}
  .card--front .watermark-circle{left:207px;top:42px;width:268px;height:268px}
  .card--back .watermark-circle{left:225px;top:42px;width:260px;height:260px}

  .brand{position:absolute;left:72px;top:70px;display:flex;align-items:center}
  .brand__dot{width:84px;height:84px;border-radius:50%;background:var(--leaf);margin-right:10px}
  .brand__name{font-family:"PT Sans",sans-serif;font-weight:700;font-size:42px;color:var(--bark);line-height:1}
  .brand__tagline{font-family:"PT Sans",sans-serif;font-size:18px;letter-spacing:1.3px;color:var(--bark);margin-top:4px}
  .brand__rule{position:absolute;left:60px;top:158px;width:572px;height:2px;background:var(--olive)}

  .person{position:absolute;left:0;top:206px;width:706px;text-align:center}
  .person__name{display:inline-block;font-size:27px;font-weight:700;color:var(--leaf);border-bottom:2px solid var(--olive);padding:0 2px 1px}
  .person__role{font-size:19px;font-weight:700;color:var(--bark);margin-top:4px}

  .contacts{position:absolute;left:0;bottom:0;height:40px;width:100%;display:flex;align-items:center;padding-left:22px;color:var(--white);font-size:15px}
  .contacts__item{display:flex;align-items:center;gap:7px}
  .contacts__sep{width:1px;height:22px;background:var(--white);margin:0 12px}
  .contacts svg{fill:none;stroke:var(--white);stroke-width:1.4}

  .programs__head{position:absolute;top:36px;left:0;width:100%;height:56px;display:flex;align-items:center;justify-content:center;
    font-size:26px;font-weight:700;color:var(--olive-dark)}
  .programs__rule{position:absolute;left:0;width:100%;background:var(--olive)}
  .programs__body{position:absolute;top:101px;left:0;width:100%;height:135px;background:rgba(134,153,58,.93);
    color:var(--white);text-align:center;padding-top:20px;line-height:1.2}
  .programs__body .sm{font-size:13px}
  .programs__body .md{font-size:15px}
  .programs__body .lg{font-size:16px;font-weight:700}
  .programs__body .xl{font-size:18px}
  .back-brand{position:absolute;top:258px;left:0;width:100%;text-align:center}
  .back-brand .brand__name{font-size:33px}
  .back-brand .brand__tagline{font-size:15px;margin-top:2px}
</style>
</head>
<body>

<section class="card card--front" aria-label="Business card front">
  <div class="band band--top"></div>
  <div class="watermark-circle" aria-hidden="true"></div>
  <div class="brand">
    <div class="brand__dot" aria-hidden="true"></div>
    <div>
      <div class="brand__name">Meridale Gardening</div>
      <div class="brand__tagline">Garden Restorations &amp; Maintenance</div>
    </div>
  </div>
  <div class="brand__rule"></div>
  <div class="person">
    <div class="person__name">Trevor Kalbrook</div>
    <div class="person__role">Horticulturalist</div>
  </div>
  <div class="band band--bottom"></div>
  <div class="contacts">
    <span class="contacts__item">
      <svg width="12" height="14" viewBox="0 0 12 14"><path d="M3 1 L5 4 L4 6 Q5 9 7 10 L9 9 L11 11 L9 13 Q2 11 1 3 Z" fill="#fff" stroke="none"/></svg>
      0452-739-186
    </span>
    <span class="contacts__sep"></span>
    <span class="contacts__item">
      <svg width="16" height="11" viewBox="0 0 16 11"><rect x="1" y="1" width="14" height="9" fill="#fff" stroke="none"/><path d="M1 1 L8 6 L15 1" stroke="#86993a"/></svg>
      meridalegard@fernpost.com
    </span>
    <span class="contacts__sep"></span>
    <span class="contacts__item">
      <svg width="16" height="16" viewBox="0 0 16 16"><circle cx="8" cy="8" r="7"/><ellipse cx="8" cy="8" rx="3" ry="7"/><path d="M1 8 H15 M2.5 4.5 H13.5 M2.5 11.5 H13.5"/></svg>
      www.meridalegardening.com.au
    </span>
  </div>
</section>

<section class="card card--back" aria-label="Business card back">
  <div class="band band--top" style="height:36px"></div>
  <div class="watermark-circle" aria-hidden="true"></div>
  <div class="programs__head">Our Maintenance Programs:</div>
  <div class="programs__rule" style="top:92px;height:5px"></div>
  <div class="programs__body">
    <div class="sm">Restore your garden to its former glory</div>
    <div class="lg">Design and cultivate your new garden or landscape</div>
    <div class="md">Make your garden more water friendly with drip irrigation</div>
    <div class="sm">Keep your indoor plants alive and thriving</div>
    <div class="xl">Grow a productive home fruit and vegie garden</div>
  </div>
  <div class="programs__rule" style="top:240px;height:5px"></div>
  <div class="back-brand">
    <div class="brand__name">Meridale Gardening</div>
    <div class="brand__tagline">Garden Restorations &amp; Maintenance</div>
  </div>
  <div class="band band--bottom"></div>
</section>

</body>
</html>
```